Billboard - Cool Garden and Landscape Company (Brand Pack Included)

NEED A PROFESSIONAL BILLBOARD TO ADVERTISE OUR BUSINESS. HAVE MOCKED UP A SAMPLE CONCEPT BUT IT REQUIRES THE ICONS TO BE DEVELOPED TO A PROFESSIONAL STANDARD (I JUST COPIED RANDOM EXAMPLES FROM THE NET)

THE ICONS REPRESENT OUR KEY PRODUCT GROUPS. (These can be redesigned)
BILLBOARD IS 6M X 3M (SEE SPEC FILE ATTACHED) - IMAGE OF THE LOCATION ADDED TO THE FILES.

BRAND GUIDE INCLUDED WITH LOGO FILES

VISIT: https://www.facebook.com/Crew.Moss.Crate/
Web: www.mosscrate.co.nz

Target Market(s)

Commuter traffic - busy road - Billboard site is on the left side approx 400m before our street turn off. Age group 30+ Home owners / Builders

Industry/Entity Type

Garden Supply

Font styles to use
Other font styles liked:
• comfortaa

Requirements
Must have
• No change to our logo or brand
• Next left
• Icons for products as per mock up - note these can be redesigned
Nice to have
• Easy to see at a distance
• Clean
• Simple

```html
<!DOCTYPE html>
<html lang="en">
<head>
<meta charset="utf-8">
<title>Mosscrate Billboard</title>
<link rel="stylesheet" href="https://fonts.googleapis.com/css2?family=Comfortaa:wght@400;700&family=Open+Sans:wght@600;700;800&display=swap">
<style>
  :root {
    --green: #2a9a45;
    --green-dark: #1d7a34;
    --orange: #ff9100;
    --orange-deep: #ff7400;
    --ink: #111111;
    --white: #ffffff;
    --backdrop: #d9d9d9;
    --tint: #f4f9e6;
  }
  * { margin: 0; padding: 0; box-sizing: border-box; }
  html, body {
    width: 1200px; height: 1200px; overflow: hidden;
    background: var(--backdrop);
  }
  .canvas { position: relative; width: 1200px; height: 1200px; }
  .billboard {
    position: absolute; left: 50px; top: 325px;
    width: 1100px; height: 550px;
    box-shadow: 0 10px 30px rgba(0,0,0,0.25);
    display: block;
  }
  .display { font-family: "Open Sans", Arial, sans-serif; }
  .brand { font-family: "Comfortaa", "Open Sans", sans-serif; }
  .headline { font-weight: 800; font-size: 56px; fill: var(--ink); }
  .address { font-weight: 600; font-size: 20px; fill: var(--ink); }
  .brand-name { font-weight: 700; font-size: 78px; fill: var(--green); }
  .tagline { font-weight: 400; font-size: 30px; fill: var(--orange); }
  .product-label { font-weight: 600; font-size: 20px; fill: var(--ink); }
  .web { font-size: 28px; fill: var(--white); font-weight: 600; }
  .web-strong { font-weight: 800; }
  .slogan { font-weight: 800; font-size: 34px; fill: var(--white); }
  .icon-ring { fill: var(--orange); stroke: #8fd39a; stroke-width: 2; }
</style>
</head>
<body>
<main class="canvas">
  <svg class="billboard" viewBox="0 0 1100 550" xmlns="http://www.w3.org/2000/svg">
    <defs>
      <linearGradient id="bg-base" x1="0" y1="0" x2="1" y2="0">
        <stop offset="0" stop-color="#eef7dc"/>
        <stop offset="0.5" stop-color="#f7fbef"/>
        <stop offset="1" stop-color="#dff0b4"/>
      </linearGradient>
      <radialGradient id="glow-a" cx="0.45" cy="0.3" r="0.35">
        <stop offset="0" stop-color="#c4e48a" stop-opacity="0.8"/>
        <stop offset="1" stop-color="#c4e48a" stop-opacity="0"/>
      </radialGradient>
      <radialGradient id="glow-b" cx="0.95" cy="0.75" r="0.35">
        <stop offset="0" stop-color="#b9de6c" stop-opacity="0.8"/>
        <stop offset="1" stop-color="#b9de6c" stop-opacity="0"/>
      </radialGradient>
    </defs>

    <!-- background -->
    <rect class="bg" width="1100" height="550" fill="url(#bg-base)"/>
    <rect width="1100" height="550" fill="url(#glow-a)"/>
    <rect width="1100" height="550" fill="url(#glow-b)"/>

    <!-- direction chevrons -->
    <g class="chevrons">
      <polygon points="124,52 184,52 112,202 184,352 124,352 52,202" fill="var(--ink)"/>
      <polygon points="130,50 190,50 118,200 190,355 130,355 58,200" fill="var(--green)"/>
      <polygon points="58,200 118,200 190,355 130,355" fill="var(--green-dark)" opacity="0.55"/>
      <polygon points="219,52 278,52 204,205 278,352 219,352 143,205" fill="var(--ink)"/>
      <polygon points="225,50 284,50 210,205 284,355 225,355 149,205" fill="var(--orange)"/>
      <polygon points="149,205 210,205 284,355 225,355" fill="var(--orange-deep)" opacity="0.7"/>
    </g>

    <!-- direction text -->
    <text class="display headline" x="53" y="415">NEXT LEFT</text>
    <text class="display address" x="55" y="442">42 Fenwick Road (off Harlow)</text>

    <!-- brand -->
    <rect class="brand-mark" x="382" y="56" width="118" height="118" fill="var(--green)"/>
    <text class="brand brand-name" x="528" y="136" textLength="505" lengthAdjust="spacingAndGlyphs">MOSSCRATE</text>
    <line x1="380" y1="183" x2="656" y2="183" stroke="var(--orange)" stroke-width="3"/>
    <text class="brand tagline" x="665" y="185" textLength="368" lengthAdjust="spacingAndGlyphs">Create Better Gardens</text>

    <!-- product groups -->
    <g class="products">
      <circle class="icon-ring" cx="440" cy="290" r="61" role="img" aria-label="Firewood and fire icon"/>
      <circle class="icon-ring" cx="617" cy="290" r="61" role="img" aria-label="Seedling in soil icon"/>
      <circle class="icon-ring" cx="793" cy="290" r="61" role="img" aria-label="Stacked stones icon"/>
      <circle class="icon-ring" cx="970" cy="290" r="61" role="img" aria-label="Trailer icon"/>

      <g class="display product-label" text-anchor="middle">
        <text x="440" y="390">Firewood</text>
        <text x="440" y="418">Fire Pellets</text>
        <text x="617" y="391">Compost</text>
        <text x="617" y="418">Soil + Mulch</text>
        <text x="793" y="389">Decorative</text>
        <text x="793" y="417">Stone Aggregates</text>
        <text x="970" y="389">Hire Trailers</text>
        <text x="970" y="417">Delivery</text>
      </g>
    </g>

    <!-- footer bands -->
    <polygon class="web-band" points="0,470 448,470 414,550 0,550" fill="var(--green)"/>
    <polygon class="slogan-band" points="466,445 1100,445 1100,550 424,550" fill="var(--orange)"/>

    <text class="display web" x="55" y="518">www.<tspan class="web-strong">mosscrate</tspan>.co.nz</text>
    <text class="display slogan" x="780" y="509" text-anchor="middle">Garden &amp; Landscape Supplies</text>
  </svg>
</main>
</body>
</html>
```